Medical Software Informational Flyer and Website Design

Our company, Copper Vale Systems, is launching a new product, the CVS Clinic Flow Platform. It is a software suite that will increase the productivity and volume of a LASIK practice.

We want this flyer to be a companion to our big reveal presentation at OPX and NVCSE; it's primary purpose is to inform potential clients on the many ways this software will help their practice. It is also obviously a promotional material. Because it is a companion to our presentation, we feel that it is acceptable for the flyer to contain much more text than would normally be reasonable in a flyer; it will go into more detail about the 12 major selling points of our software than our presentation time will allow. Having said that, however, we still want there to be "breathing room" for the design and the viewer's eyes.

We have uploaded our logo, both in full color and in white with no background (often used for watermarks, but certainly not restricted for that use alone). Our logo should be accompanied by either "Copper Vale Systems" or "CVS" using the Trajan Pro font (unoriginal, we know, but it's what we've chosen). We have included a color palette that compliments our logo, but designs are not limited to that palette (for example, we have found a pink (#cc1448) that compliments the palette and that we have used in the presentation).

We have also uploaded a PSD that includes icons that could compliment 9 of the 12 major selling points for the CVS Clinic Flow Platform software (the category titles are subject to change). The icons are not necessarily set in stone. For consistency with our presentation, the Protection, Integration, and Review icons should be used, but any of the remaining six (in particular, the Personalized icon) can be changed to whatever you think might be more suitable. The PSD also has some preliminary text for a few of the 12 selling points (we are refining the text now and will get the final content to designers very soon). Also note that the font is simply a placeholder; use whatever font you think would best compliment your design. Finally, keep in mind that the PSD does NOT reflect a design we are looking for; in fact, we hate this "design" and hesitate to call it a design. It was simply a way to arrange the elements to easily distribute them to designers.

We want an 8 1/2in x 11in 8-page flyer that is professional, simple, and has a clear message: this product will revolutionize your practice! We of course also need a website design that compliments the flyer design once the flyer design is finalized and chosen.

We will be monitoring this project closely-- please ask any questions you have!
Updates

Target Market(s)

Physicians, technicians, and marketing personnel in the LASIK industry.

Industry/Entity Type

Software

Number of Pages Required

4 page

Font styles to use
Serif
Sans Serif

```html
<!DOCTYPE html>
<html lang="en">
<head>
<meta charset="utf-8">
<title>Copper Vale Systems – CVS Clinic Flow Platform</title>
<link href="https://fonts.googleapis.com/css2?family=Cinzel:wght@500;600&family=Lato:wght@400&display=swap" rel="stylesheet">
<style>
  :root {
    --page-bg: #e7e2da;
    --sun-yellow: #fbe21b;
    --leaf-green: #bfd83b;
    --deep-navy: #0d3a4f;
    --brand-teal: #1b8a6b;
    --text-light: #ffffff;
    --text-dark: #0f2e3c;
  }
  * { margin: 0; padding: 0; box-sizing: border-box; }
  html, body {
    width: 958px; height: 1200px; overflow: hidden;
    background: var(--page-bg);
  }
  .flyer-frame {
    position: absolute; left: 15px; top: 0;
    width: 928px; height: 1200px; overflow: hidden;
  }
  .flyer {
    position: absolute; left: 0; top: 0;
    width: 1048px; height: 1355px;
    transform: scale(0.8856); transform-origin: 0 0;
    background: var(--sun-yellow);
  }
  .flyer-shapes { position: absolute; inset: 0; width: 1048px; height: 1355px; }

  .brand {
    position: absolute; left: 258px; top: 20px;
    display: flex; align-items: center; gap: 18px;
  }
  .brand-square {
    width: 135px; height: 135px;
    background: var(--deep-navy);
    border: 9px solid #ffffff;
  }
  .brand-name {
    font-family: "Cinzel", serif; font-weight: 600;
    font-size: 58px; line-height: 60px; letter-spacing: 4px;
    color: var(--deep-navy);
  }

  .suite-title {
    position: absolute; left: 0; right: 0; top: 742px;
    text-align: center;
    font-family: "Cinzel", serif; font-weight: 600;
    font-size: 39px; letter-spacing: 4px;
    color: var(--deep-navy);
  }
  .intro {
    position: absolute; left: 74px; width: 900px; top: 817px;
    text-align: center;
    font-family: "Lato", sans-serif; font-size: 19.5px; line-height: 31px;
    color: var(--text-light);
  }
  .intro p + p { margin-top: 17px; }

  .contact-watermark {
    position: absolute; left: 631px; top: 1284px;
    width: 58px; height: 57px;
    border: 3px solid rgba(255,255,255,0.55);
  }
  .contact {
    position: absolute; right: 63px; top: 1262px;
    font-family: "Lato", sans-serif; font-size: 13.5px; color: var(--text-dark);
    display: flex; flex-direction: column; align-items: flex-end; gap: 11px;
  }
  .contact-row { display: flex; align-items: center; gap: 28px; }
  .contact-item { display: flex; align-items: center; gap: 7px; white-space: nowrap; }
  .contact-item svg { width: 16px; height: 16px; }
</style>
</head>
<body>
<div class="flyer-frame">
  <div class="flyer">
    <svg class="flyer-shapes" viewBox="0 0 1048 1355" aria-hidden="true">
      <defs>
        <linearGradient id="skyScene" x1="0" y1="0" x2="0" y2="1">
          <stop offset="0" stop-color="#7ea7d6"/>
          <stop offset="0.35" stop-color="#d9e6f2"/>
          <stop offset="0.68" stop-color="#eef2f1"/>
          <stop offset="0.84" stop-color="#86a25a"/>
          <stop offset="1" stop-color="#476f2c"/>
        </linearGradient>
      </defs>
      <!-- green body -->
      <rect x="0" y="560" width="1048" height="795" fill="var(--leaf-green)"/>
      <!-- top navy swoosh -->
      <path d="M0,210 C160,188 360,176 535,176 C360,182 160,205 0,238 Z" fill="var(--deep-navy)"/>
      <!-- bottom right navy swoosh -->
      <path d="M515,700 C700,700 900,672 1048,624 L1048,646 C900,688 700,704 515,700 Z" fill="var(--deep-navy)"/>
      <!-- bottom yellow -->
      <path d="M0,1300 C330,1300 700,1245 1048,1175 L1048,1355 L0,1355 Z" fill="var(--sun-yellow)"/>
      <!-- bottom left navy swoosh -->
      <path d="M0,1262 C160,1292 360,1290 505,1272 C360,1300 160,1310 0,1292 Z" fill="var(--deep-navy)"/>
    </svg>

    <svg class="flyer-shapes" viewBox="0 0 1048 1355" role="img" aria-label="Photo of a hiker with outstretched arms on a rock ledge above green hills under a bright blue cloudy sky">
      <path d="M0,252 Q524,128 1048,252 L1048,625 Q524,760 0,622 Z" fill="url(#skyScene)"/>
    </svg>

    <div class="brand">
      <div class="brand-square"></div>
      <div class="brand-name">Copper Vale<br>Systems</div>
    </div>

    <h1 class="suite-title">The CVS Clinic Flow Platform</h1>

    <div class="intro">
      <p>To remain competitive in the arena of elective surgery the list of “must haves” seems endless. Worse yet, the tools to execute and deliver on that list either don’t exist or run on assorted disconnected devices or systems.</p>
      <p>Copper Vale Systems’ Practice Management Suite represents a truly revolutionary solution to successfully managing a refractive business. The CVS practice management toolset provides users with the ability to enjoy end-to-end lead tracking for improved prospect conversions; the ability to communicate personally and securely with prospects and patients; it provides the processes needed to deliver a truly personalized patient experience; it delivers the capacity to invigorate, empower, and sustain word-of-mouth referrals.</p>
      <p>See for yourself and envision how CVS can change your practice for the better today!</p>
    </div>

    <div class="contact-watermark"></div>
    <div class="contact">
      <div class="contact-row">
        <span class="contact-item">123-456-7890
          <svg viewBox="0 0 16 16"><path d="M3,1 L6,1 L7,5 L5,6.5 C6,9 7.5,10.5 10,11.5 L11.5,9.5 L15,10.5 L15,13.5 C15,14.5 14,15 13,15 C6.5,14.5 1.5,9.5 1,3 C1,2 2,1 3,1 Z" fill="var(--brand-teal)"/></svg>
        </span>
        <span class="contact-item">info@coppervale.com
          <svg viewBox="0 0 16 16"><rect x="1" y="3" width="14" height="10" fill="none" stroke="var(--brand-teal)" stroke-width="1.4"/><path d="M1,3 L8,9 L15,3" fill="none" stroke="var(--brand-teal)" stroke-width="1.4"/></svg>
        </span>
      </div>
      <span class="contact-item">www.coppervale.com
        <svg viewBox="0 0 16 16"><g fill="none" stroke="var(--brand-teal)" stroke-width="1.2"><circle cx="8" cy="8" r="6.5"/><ellipse cx="8" cy="8" rx="3" ry="6.5"/><path d="M1.5,8 H14.5 M2.5,4.8 H13.5 M2.5,11.2 H13.5"/></g></svg>
      </span>
      <span class="contact-item">Lorem ipsum dolor sit, Zip Code-1234567
        <svg viewBox="0 0 16 16"><path d="M8,1 C5,1 3,3.2 3,6 C3,9.5 8,15 8,15 C8,15 13,9.5 13,6 C13,3.2 11,1 8,1 Z" fill="var(--brand-teal)"/><circle cx="8" cy="6" r="2" fill="var(--sun-yellow)"/></svg>
      </span>
    </div>
  </div>
</div>
</body>
</html>
```